E-Book/ Buch-Cover spannenden Liebesroman gesucht.
Zielgruppe
Ich bin Autorin und suche ein ansprechendes Cover für mein E-Book mit dem Titel:
' Schattenhafte Reue'. Es handelt sich um einen spannenden Liebesroman. Die emotionalen Ängste des Protagonisten, stehen neben den offensichtlichen Bedrohungen der Hauptfigur. Beide müssen ihren Weg zu einem Happyend finden. Da der Titel schon etwas „schreit“, sollte das Cover diesen Eindruck eventuell etwas abfedern.
Aufgabenstellung
Kein Kitsch, kein Schnulzencover, es handelt sich bei aller Dramatik trotzdem um einen Liebesroman. Keinen Thriller.

```html
<!DOCTYPE html>
<html lang="de">
<head>
<meta charset="utf-8">
<title>Schattenhafte Reue – Cover</title>
<link rel="stylesheet" href="https://fonts.googleapis.com/css2?family=Bodoni+Moda:wght@400;500&display=swap">
<style>
  :root {
    --page-bg: #e9e9e8;
    --sky-top: #0d2328;
    --sky-teal: #3f6870;
    --sky-haze: #7f9ba0;
    --sky-rose: #b38a88;
    --sky-ember: #d2653f;
    --ground: #050607;
    --ink-light: #ffffff;
  }
  * { margin: 0; padding: 0; box-sizing: border-box; }
  html, body {
    width: 1200px;
    height: 800px;
    overflow: hidden;
    background: var(--page-bg);
  }
  .canvas {
    position: relative;
    width: 1200px;
    height: 800px;
  }
  .book-cover {
    position: absolute;
    left: 355px;
    top: 18px;
    width: 490px;
    height: 764px;
    overflow: hidden;
    font-family: "Bodoni Moda", "Didot", serif;
    font-weight: 400;
    color: var(--ink-light);
  }
  .cover-photo {
    position: absolute;
    inset: 0;
    background: linear-gradient(
      to bottom,
      var(--sky-top) 0%,
      var(--sky-teal) 28%,
      var(--sky-haze) 48%,
      var(--sky-rose) 60%,
      var(--sky-ember) 67%,
      #3a1a12 71%,
      var(--ground) 75%,
      var(--ground) 100%
    );
  }
  .title {
    font-weight: 400;
  }
  .title-line,
  .title-main {
    position: absolute;
    right: 35px;
    line-height: 1;
    white-space: nowrap;
  }
  .title-line {
    top: 56px;
    font-size: 58px;
    letter-spacing: -0.5px;
  }
  .title-main {
    top: 90px;
    font-size: 190px;
    letter-spacing: -4px;
  }
  .genre {
    position: absolute;
    left: 342px;
    top: 317px;
    font-size: 29px;
    line-height: 1;
  }
  .author {
    position: absolute;
    left: 0;
    width: 490px;
    top: 621px;
    text-align: center;
    font-size: 44px;
    line-height: 1;
    letter-spacing: -0.5px;
  }
</style>
</head>
<body>
  <main class="canvas">
    <section class="book-cover">
      <div class="cover-photo" role="img" aria-label="Coverfoto: Abendhimmel in Blaugrün und Orange über dunklem Land"></div>
      <h1 class="title">
        <span class="title-line">Schattenhafte</span>
        <span class="title-main">Reue</span>
      </h1>
      <p class="genre">roman</p>
      <p class="author">c.m. sternfeld</p>
    </section>
  </main>
</body>
</html>
```